Lumo Sourdough Tortilla bag design front and back

Our tortilla bags are flat plastic bags. I would like a design for the front and back of our tortillas. Our tortillas are made of whole wheat flour. We have decided to go with the following font and color scheme for our tortilla bags from the updated attached samples below. Wheat or taco images are okay to brighten and make the package stand out. We prefer a clean look. We prefer the word "Artisian" to remain in cursive.

Target Market(s)

Health conscious consumers

Industry/Entity Type

Bakery

Font styles to use
Serif
Sans Serif
Decorative

Colors
59FF00
82FF00
B8FF75
E3FFCB
F4FFEA
EB3D1F
EC4F4E
F09395
F8D3D4
FCEDEE

Requirements
Must have
• The word "sourdough must standout and be prominent on the front,
Nice to have
• Looking for clean upscale look that pops

```html
<!DOCTYPE html>
<html lang="en">
<head>
<meta charset="utf-8">
<title>Lumo Sourdough Tortilla – Bag Front and Back</title>
<link href="https://fonts.googleapis.com/css2?family=Cinzel:wght@400;500&family=Josefin+Sans:wght@300;400&family=Oswald:wght@400;500&family=Roboto+Condensed:wght@400;700;900&display=swap" rel="stylesheet">
<style>
  :root {
    --backdrop: #3d2c26;
    --leaf-green: #a8c94b;
    --title-green: #b9d65c;
    --charcoal: #262626;
    --ink: #1b1b1b;
    --soft-text: #e6e6e6;
    --pouch-white: #e8e8e6;
    --panel-w: 241px;
    --panel-h: 374px;
  }
  * { box-sizing: border-box; margin: 0; padding: 0; }
  html, body { width: 1200px; height: 458px; overflow: hidden; }
  body { background: var(--backdrop); position: relative; font-family: "Josefin Sans", sans-serif; }

  .bag { position: absolute; top: 38px; width: var(--panel-w); height: var(--panel-h); overflow: hidden; }
  .bag--front { left: 48px; }
  .bag--back-light { left: 329px; background: var(--pouch-white); }
  .bag--back-green { left: 619px; background: var(--leaf-green); }
  .bag--back-band { left: 900px; background: var(--pouch-white); }

  .band { position: absolute; left: 0; right: 0; }
  .band--green { background: var(--leaf-green); }
  .band--charcoal { background: var(--charcoal); }
  .band--gold { background: linear-gradient(90deg, #8e7b4c, #d9c894, #8e7b4c); }
  .band--black { background: #111; }

  .zipper { position: absolute; left: 10px; right: 10px; top: 38px; height: 4px; border-radius: 2px; background: rgba(255,255,255,.45); }

  /* Front */
  .brand-seal { position: absolute; left: 88px; top: 25px; width: 64px; height: 64px; border-radius: 50%; background: var(--charcoal);
    display: flex; align-items: center; justify-content: center; font-family: "Cinzel", serif; font-size: 15px; color: var(--leaf-green); letter-spacing: .5px; }
  .salt-flag { position: absolute; left: 197px; top: 13px; width: 34px; height: 34px; border-radius: 50%; background: var(--charcoal);
    color: #fff; font-size: 5.2px; line-height: 6.6px; text-align: center; display: flex; align-items: center; justify-content: center; padding-top: 1px; }
  .rule { position: absolute; height: 1px; background: var(--title-green); opacity: .7; }
  .product-name { position: absolute; left: 0; right: 0; top: 172px; text-align: center; font-family: "Cinzel", serif; font-weight: 400; font-size: 26px; line-height: 30px; color: var(--title-green); letter-spacing: .3px; }
  .product-style { position: absolute; left: 0; right: 0; top: 292px; text-align: center; font-size: 8.5px; letter-spacing: 5px; color: var(--ink); padding-left: 5px; }
  .product-type { position: absolute; left: 0; right: 0; top: 303px; text-align: center; font-family: "Oswald", sans-serif; font-weight: 500; font-size: 28px; line-height: 32px; color: var(--ink); transform: scaleX(.78); }
  .fine-print { position: absolute; font-family: "Roboto Condensed", sans-serif; font-size: 3.8px; line-height: 4.4px; color: var(--ink); text-align: center; }
  .badge { position: absolute; width: 17px; height: 17px; border-radius: 50%; background: var(--ink); }

  /* Back story */
  .story { position: absolute; top: 117px; display: block; }
  .story__title { font-family: "Cinzel", serif; font-weight: 400; font-size: 12px; line-height: 14px; color: var(--title-green); margin-bottom: 4px; white-space: nowrap; }
  .story__text { font-weight: 300; font-size: 5.8px; line-height: 10.2px; color: var(--soft-text); white-space: nowrap; }
  .story--left { left: 34px; width: 80px; }
  .story--centered { left: 20px; width: 102px; text-align: center; }
  .story--dark .story__text, .story--dark .story__title { color: var(--ink); }
  .story__rule { margin: 8px auto 0; width: 62px; height: 1px; background: var(--title-green); }
  .story--dark .story__rule { background: var(--ink); }

  .label-column { position: absolute; left: 131px; top: 120px; width: 74px; color: var(--soft-text); }
  .label-column--dark { color: var(--ink); }
  .ingredients { font-size: 3.8px; line-height: 5px; margin-bottom: 4px; }
  .maker { font-size: 3.6px; line-height: 5.6px; margin-top: 5px; }

  .nutrition { background: #fff; color: #000; border: 1px solid #000; padding: 1.5px 2px; font-family: "Roboto Condensed", sans-serif; width: 72px; }
  .nutrition__title { font-weight: 900; font-size: 8.6px; line-height: 9px; border-bottom: .5px solid #000; white-space: nowrap; }
  .nutrition__row { display: flex; justify-content: space-between; font-size: 3.4px; line-height: 4.5px; border-bottom: .4px solid #000; white-space: nowrap; }
  .nutrition__row--plain { border-bottom: none; }
  .nutrition__row--thick { border-bottom: 2.5px solid #000; }
  .nutrition__row--right { justify-content: flex-end; }
  .nutrition__row--indent { padding-left: 4px; }
  .nutrition__row--indent2 { padding-left: 9px; }
  .nutrition__calories { display: flex; justify-content: space-between; align-items: flex-end; font-weight: 900; font-size: 8px; line-height: 9px; border-bottom: 1.5px solid #000; }
  .nutrition__small { font-size: 2.8px; line-height: 3.4px; }
  .nutrition__small--ruled { border-top: .4px solid #000; margin-top: 1px; }
  .b { font-weight: 700; }
</style>
</head>
<body>

<!-- Front of bag -->
<section class="bag bag--front" aria-label="Bag front">
  <div class="band band--green" style="top:0;height:100px" role="img" aria-label="Green band with subtle floral pattern"></div>
  <div class="band band--gold" style="top:100px;height:6px"></div>
  <div class="band band--charcoal" style="top:106px;height:170px" role="img" aria-label="Charcoal band with faint floral pattern"></div>
  <div class="band band--gold" style="top:276px;height:6px"></div>
  <div class="band band--green" style="top:282px;height:92px" role="img" aria-label="Green band with subtle floral pattern"></div>

  <div class="brand-seal">LUMO</div>
  <div class="salt-flag">NO<br>ADDED<br>SALT</div>

  <div class="rule" style="left:14px;width:213px;top:163px"></div>
  <h1 class="product-name">SOURDOUGH</h1>
  <div class="rule" style="left:14px;width:213px;top:220px"></div>

  <p class="product-style">ARTISIAN</p>
  <p class="product-type">TORTILLAS</p>

  <p class="fine-print" style="left:10px;top:356px">KEEP FROZEN</p>
  <div class="badge" style="left:61px;top:348px" aria-label="Vegan badge"></div>
  <div class="badge" style="left:99px;top:348px" aria-label="Kosher badge"></div>
  <div class="badge" style="left:136px;top:348px" aria-label="No soy badge"></div>
  <p class="fine-print" style="left:182px;top:350px">8 CT<br>NET WEIGHT<br>12 OUNCES/243 G</p>
</section>

<!-- Back, light pouch -->
<section class="bag bag--back-light" aria-label="Bag back, light version">
  <div class="zipper"></div>
  <div class="band band--green" style="top:98px;height:6px"></div>
  <div class="band band--charcoal" style="top:104px;height:172px"></div>
  <div class="band band--green" style="top:276px;height:6px"></div>

  <div class="story story--left">
    <h2 class="story__title">Our Story</h2>
    <p class="story__text">Lumo sourdough tortillas<br>and flatbreads are made<br>with organically grown<br>stone ground whole<br>wheat and nothing<br>artificial. Our dough is<br>naturally fermented<br>over 48 hours to<br>produce not only the<br>BEST TASTING but the<br>MOST NUTRITIOUS<br>tortillas and flatbreads<br>on the market today!</p>
  </div>

  <div class="label-column">
    <p class="ingredients">Ingredients: Stone ground whole wheat, Purified water, olive oil, wild yeast</p>
    <div class="nutrition">
      <div class="nutrition__title">Nutrition Facts</div>
      <div class="nutrition__row nutrition__row--plain">8 servings per container</div>
      <div class="nutrition__row nutrition__row--thick b"><span>Serving size</span><span>1 (50g)</span></div>
      <div class="nutrition__row nutrition__row--plain"><span class="b">Amount Per Serving</span></div>
      <div class="nutrition__calories"><span>Calories</span><span>150</span></div>
      <div class="nutrition__row nutrition__row--right">% Daily Value*</div>
      <div class="nutrition__row"><span><span class="b">Total Fat</span> 2g</span><span>3%</span></div>
      <div class="nutrition__row nutrition__row--indent"><span>Saturated Fat 0g</span><span>0%</span></div>
      <div class="nutrition__row nutrition__row--indent"><span><i>Trans</i> Fat 0g</span><span></span></div>
      <div class="nutrition__row"><span><span class="b">Cholesterol</span> 0mg</span><span>0%</span></div>
      <div class="nutrition__row"><span><span class="b">Sodium</span> 150mg</span><span>7%</span></div>
      <div class="nutrition__row"><span><span class="b">Total Carbohydrate</span> 25g</span><span>9%</span></div>
      <div class="nutrition__row nutrition__row--indent"><span>Dietary Fiber 3g</span><span>11%</span></div>
      <div class="nutrition__row nutrition__row--indent"><span>Total Sugars 0g</span><span></span></div>
      <div class="nutrition__row nutrition__row--indent2"><span>Includes 0g Added Sugars</span><span>0%</span></div>
      <div class="nutrition__row nutrition__row--thick"><span><span class="b">Protein</span> 4g</span><span>8%</span></div>
      <p class="nutrition__small">Not a significant source of vitamin D, calcium, iron, and potassium</p>
      <p class="nutrition__small nutrition__small--ruled">*% Daily Value based on a 2,000 calorie diet.</p>
    </div>
    <p class="maker">Manufactured:<br>Hearthline Bread Co. LLC,</p>
  </div>
</section>

<!-- Back, green pouch -->
<section class="bag bag--back-green" aria-label="Bag back, green version">
  <div class="band band--green" style="top:0;height:100px" role="img" aria-label="Green band with subtle floral pattern"></div>
  <div class="zipper"></div>
  <div class="band band--gold" style="top:100px;height:6px"></div>
  <div class="band band--charcoal" style="top:106px;height:172px" role="img" aria-label="Charcoal band with faint floral pattern"></div>
  <div class="band band--gold" style="top:278px;height:6px"></div>

  <div class="story story--centered" style="top:124px">
    <h2 class="story__title">Our Story</h2>
    <p class="story__text">Lumo sourdough tortillas<br>and flatbreads are made<br>with organically grown<br>stone ground whole wheat<br>and nothing artificial. Our<br>dough is naturally<br>fermented over 48 hours<br>to produce not only the<br>BEST TASTING but the<br>MOST NUTRITIOUS<br>tortillas and flatbreads on<br>the market today!</p>
    <div class="story__rule"></div>
  </div>

  <div class="label-column" style="top:128px">
    <p class="ingredients">Ingredients: Stone ground whole wheat, Purified water, olive oil, wild yeast</p>
    <div class="nutrition">
      <div class="nutrition__title">Nutrition Facts</div>
      <div class="nutrition__row nutrition__row--plain">8 servings per container</div>
      <div class="nutrition__row nutrition__row--thick b"><span>Serving size</span><span>1 (50g)</span></div>
      <div class="nutrition__row nutrition__row--plain"><span class="b">Amount Per Serving</span></div>
      <div class="nutrition__calories"><span>Calories</span><span>150</span></div>
      <div class="nutrition__row nutrition__row--right">% Daily Value*</div>
      <div class="nutrition__row"><span><span class="b">Total Fat</span> 2g</span><span>3%</span></div>
      <div class="nutrition__row nutrition__row--indent"><span>Saturated Fat 0g</span><span>0%</span></div>
      <div class="nutrition__row nutrition__row--indent"><span><i>Trans</i> Fat 0g</span><span></span></div>
      <div class="nutrition__row"><span><span class="b">Cholesterol</span> 0mg</span><span>0%</span></div>
      <div class="nutrition__row"><span><span class="b">Sodium</span> 150mg</span><span>7%</span></div>
      <div class="nutrition__row"><span><span class="b">Total Carbohydrate</span> 25g</span><span>9%</span></div>
      <div class="nutrition__row nutrition__row--indent"><span>Dietary Fiber 3g</span><span>11%</span></div>
      <div class="nutrition__row nutrition__row--indent"><span>Total Sugars 0g</span><span></span></div>
      <div class="nutrition__row nutrition__row--indent2"><span>Includes 0g Added Sugars</span><span>0%</span></div>
      <div class="nutrition__row nutrition__row--thick"><span><span class="b">Protein</span> 4g</span><span>8%</span></div>
      <p class="nutrition__small">Not a significant source of vitamin D, calcium, iron, and potassium</p>
      <p class="nutrition__small nutrition__small--ruled">*% Daily Value based on a 2,000 calorie diet.</p>
    </div>
    <p class="maker">Manufactured:<br>Hearthline Bread Co. LLC,</p>
  </div>

  <div class="badge" style="left:42px;top:348px" aria-label="Vegan badge"></div>
  <div class="badge" style="left:82px;top:348px" aria-label="Kosher badge"></div>
  <div class="badge" style="left:123px;top:348px" aria-label="No soy badge"></div>
  <div class="badge" style="left:163px;top:348px" aria-label="Keep frozen badge"></div>
</section>

<!-- Back, light pouch with green band -->
<section class="bag bag--back-band" aria-label="Bag back, banded version">
  <div class="zipper"></div>
  <div class="band band--black" style="top:99px;height:6px"></div>
  <div class="band band--green" style="top:105px;height:174px" role="img" aria-label="Green band with subtle floral pattern"></div>
  <div class="band band--black" style="top:279px;height:7px"></div>

  <div class="story story--centered story--dark" style="top:124px">
    <h2 class="story__title">Our Story</h2>
    <p class="story__text">Lumo sourdough tortillas<br>and flatbreads are made<br>with organically grown<br>stone ground whole wheat<br>and nothing artificial. Our<br>dough is naturally<br>fermented over 48 hours<br>to produce not only the<br>BEST TASTING but the<br>MOST NUTRITIOUS<br>tortillas and flatbreads on<br>the market today!</p>
    <div class="story__rule"></div>
  </div>

  <div class="label-column label-column--dark" style="top:128px">
    <p class="ingredients">Ingredients: Stone ground whole wheat, Purified water, olive oil, wild yeast</p>
    <div class="nutrition">
      <div class="nutrition__title">Nutrition Facts</div>
      <div class="nutrition__row nutrition__row--plain">8 servings per container</div>
      <div class="nutrition__row nutrition__row--thick b"><span>Serving size</span><span>1 (50g)</span></div>
      <div class="nutrition__row nutrition__row--plain"><span class="b">Amount Per Serving</span></div>
      <div class="nutrition__calories"><span>Calories</span><span>150</span></div>
      <div class="nutrition__row nutrition__row--right">% Daily Value*</div>
      <div class="nutrition__row"><span><span class="b">Total Fat</span> 2g</span><span>3%</span></div>
      <div class="nutrition__row nutrition__row--indent"><span>Saturated Fat 0g</span><span>0%</span></div>
      <div class="nutrition__row nutrition__row--indent"><span><i>Trans</i> Fat 0g</span><span></span></div>
      <div class="nutrition__row"><span><span class="b">Cholesterol</span> 0mg</span><span>0%</span></div>
      <div class="nutrition__row"><span><span class="b">Sodium</span> 150mg</span><span>7%</span></div>
      <div class="nutrition__row"><span><span class="b">Total Carbohydrate</span> 25g</span><span>9%</span></div>
      <div class="nutrition__row nutrition__row--indent"><span>Dietary Fiber 3g</span><span>11%</span></div>
      <div class="nutrition__row nutrition__row--indent"><span>Total Sugars 0g</span><span></span></div>
      <div class="nutrition__row nutrition__row--indent2"><span>Includes 0g Added Sugars</span><span>0%</span></div>
      <div class="nutrition__row nutrition__row--thick"><span><span class="b">Protein</span> 4g</span><span>8%</span></div>
      <p class="nutrition__small">Not a significant source of vitamin D, calcium, iron, and potassium</p>
      <p class="nutrition__small nutrition__small--ruled">*% Daily Value based on a 2,000 calorie diet.</p>
    </div>
    <p class="maker">Manufactured:<br>Hearthline Bread Co. LLC,</p>
  </div>
</section>

</body>
</html>
```